Business Card for Toffee Parlour

I have a logo for my candy buffet business, and need a business card designed using that logo. Toffee Parlour designs and builds beautiful and delicious candy and dessert tables for all kinds of events. The card should be simple, modern, graphic, colorful, and use the Toffee Parlour Logo.

Target Market(s)

The target market is people hosting major parties and events. This includes brides getting married, parents hosting birthday parties/Sweet Sixteen/Bar Mitzvah/quinceanera parties, and companies hosting corporate events.

Industry/Entity Type

Business

Requirements
Must have
• The business card must have the logo, with or without the tag line.

The following information must be on the card:

Renata Hollis
CEO & Candy Stylist
415.372.6091
renata@toffeeparlourco.example
Nice to have
• I like the idea of having multiple colors of the same design so that several people receiving cards will each receive a different color. Perhaps 3-5 colors or variations on a basic card design.

```html
<!DOCTYPE html>
<html lang="en">
<head>
<meta charset="utf-8">
<title>Toffee Parlour – Business Cards</title>
<link rel="stylesheet" href="https://fonts.googleapis.com/css2?family=Questrial&display=swap">
<style>
  :root {
    --stage: #1e1e1e;
    --stripe-green: #0f9447;
    --stripe-orange: #f2a935;
    --stripe-blue: #2a96b8;
    --stripe-pink: #e0287a;
    --ink: #111111;
    --white: #ffffff;
    --peach-light: #fff6e8;
    --peach-deep: #f3b461;
    --sky-light: #f4fbff;
    --sky-deep: #5fb7e4;
    --mint-light: #f3fbef;
    --mint-deep: #6fbf6a;
    --lilac-light: #fbf8ff;
    --lilac-deep: #9c8fc8;
    --dot: #e0287a;
  }
  * { box-sizing: border-box; margin: 0; padding: 0; }
  html, body { width: 1200px; height: 1016px; overflow: hidden; }
  body {
    background: var(--stage);
    font-family: "Questrial", "Century Gothic", sans-serif;
    color: var(--ink);
    position: relative;
  }

  .card {
    position: absolute;
    overflow: hidden;
    display: flex;
    flex-direction: column;
    box-shadow: 0 6px 18px rgba(0,0,0,.5);
  }
  .card--large { width: 530px; height: 310px; top: 190px; }
  .card--small { width: 350px; height: 210px; top: 767px; }
  .card--back  { left: 45px; }
  .card--front { left: 625px; }
  .card--sky   { left: 50px; }
  .card--mint  { left: 421px; }
  .card--lilac { left: 792px; }

  .card--peach { background: radial-gradient(ellipse at 50% 45%, var(--peach-light) 15%, var(--peach-deep) 100%); }
  .card--sky   { background: radial-gradient(ellipse at 45% 45%, var(--sky-light) 20%, var(--sky-deep) 110%); }
  .card--mint  { background: radial-gradient(ellipse at 45% 45%, var(--mint-light) 20%, var(--mint-deep) 110%); }
  .card--lilac { background: radial-gradient(ellipse at 45% 45%, var(--lilac-light) 20%, var(--lilac-deep) 110%); }

  .stripes { display: flex; flex-direction: column; flex: none; }
  .stripe { display: block; }
  .card--large .stripe { height: 7px; }
  .card--small .stripe { height: 5px; }
  .stripe + .stripe { margin-top: 2px; }
  .stripe--green  { background: var(--stripe-green); }
  .stripe--orange { background: var(--stripe-orange); }
  .stripe--blue   { background: var(--stripe-blue); }
  .stripe--pink   { background: var(--stripe-pink); }

  .brand {
    flex: 1;
    display: flex;
    align-items: center;
    justify-content: center;
  }
  .brand__name {
    display: flex;
    align-items: center;
    gap: .35em;
    line-height: 1;
    letter-spacing: -.01em;
    white-space: nowrap;
  }
  .brand__dot {
    width: .62em; height: .62em;
    border-radius: 50%;
    background: var(--dot);
  }
  .card--large .brand__name { font-size: 46px; }
  .card--small .brand__name { font-size: 27px; }
  .card--back .brand__name { font-size: 38px; }

  .contact { flex: none; display: flex; flex-direction: column; }
  .contact__band {
    height: 30px;
    display: flex;
    align-items: center;
    gap: 10px;
    padding-left: 28px;
    color: var(--white);
    font-size: 14px;
    letter-spacing: .02em;
    white-space: nowrap;
  }
  .contact__band--pink  { background: var(--stripe-pink); }
  .contact__band--blue  { background: var(--stripe-blue); }
  .contact__band--green { background: var(--stripe-green); }
  .contact__name { font-weight: 700; text-transform: uppercase; }
  .contact__role { text-transform: uppercase; }
  .contact__icon { width: 18px; height: 14px; flex: none; }
</style>
</head>
<body>

  <!-- Back: contact side -->
  <article class="card card--large card--back card--peach">
    <div class="stripes">
      <span class="stripe stripe--green"></span>
      <span class="stripe stripe--orange"></span>
      <span class="stripe stripe--pink"></span>
    </div>
    <div class="brand">
      <p class="brand__name"><span class="brand__dot"></span>Toffee Parlour</p>
    </div>
    <div class="contact">
      <p class="contact__band contact__band--pink">
        <span class="contact__name">Renata Hollis</span>
        <span class="contact__role">– CEO &amp; Candy Stylist</span>
      </p>
      <p class="contact__band contact__band--blue">
        <svg class="contact__icon" viewBox="0 0 18 14" aria-hidden="true">
          <rect x="1" y="1" width="16" height="12" fill="none" stroke="#fff" stroke-width="1.4"/>
          <path d="M1 1 L9 8 L17 1" fill="none" stroke="#fff" stroke-width="1.4"/>
        </svg>
        renata@toffeeparlourco.example
      </p>
      <p class="contact__band contact__band--green">
        <svg class="contact__icon" viewBox="0 0 18 14" aria-hidden="true">
          <path d="M5 1 L7.5 4 L6 6 Q8 9 11 10 L13 8.5 L16 11 L14 13 Q6 12 3 3 Z" fill="#fff"/>
        </svg>
        415.372.6091
      </p>
    </div>
  </article>

  <!-- Front: logo side -->
  <article class="card card--large card--front card--peach">
    <div class="stripes">
      <span class="stripe stripe--green"></span>
      <span class="stripe stripe--orange"></span>
      <span class="stripe stripe--pink"></span>
    </div>
    <div class="brand">
      <p class="brand__name"><span class="brand__dot"></span>Toffee Parlour</p>
    </div>
    <div class="stripes">
      <span class="stripe stripe--green"></span>
      <span class="stripe stripe--orange"></span>
      <span class="stripe stripe--blue"></span>
      <span class="stripe stripe--pink"></span>
    </div>
  </article>

  <!-- Colour variants -->
  <article class="card card--small card--sky">
    <div class="stripes">
      <span class="stripe stripe--green"></span>
      <span class="stripe stripe--orange"></span>
      <span class="stripe stripe--pink"></span>
    </div>
    <div class="brand">
      <p class="brand__name"><span class="brand__dot"></span>Toffee Parlour</p>
    </div>
    <div class="stripes">
      <span class="stripe stripe--green"></span>
      <span class="stripe stripe--orange"></span>
      <span class="stripe stripe--blue"></span>
      <span class="stripe stripe--pink"></span>
    </div>
  </article>

  <article class="card card--small card--mint">
    <div class="stripes">
      <span class="stripe stripe--green"></span>
      <span class="stripe stripe--orange"></span>
      <span class="stripe stripe--pink"></span>
    </div>
    <div class="brand">
      <p class="brand__name"><span class="brand__dot"></span>Toffee Parlour</p>
    </div>
    <div class="stripes">
      <span class="stripe stripe--green"></span>
      <span class="stripe stripe--orange"></span>
      <span class="stripe stripe--blue"></span>
      <span class="stripe stripe--pink"></span>
    </div>
  </article>

  <article class="card card--small card--lilac">
    <div class="stripes">
      <span class="stripe stripe--green"></span>
      <span class="stripe stripe--orange"></span>
      <span class="stripe stripe--pink"></span>
    </div>
    <div class="brand">
      <p class="brand__name"><span class="brand__dot"></span>Toffee Parlour</p>
    </div>
    <div class="stripes">
      <span class="stripe stripe--green"></span>
      <span class="stripe stripe--orange"></span>
      <span class="stripe stripe--blue"></span>
      <span class="stripe stripe--pink"></span>
    </div>
  </article>

</body>
</html>
```